Book Cover for Christian book about open-air preaching

The book is about open-air or outdoor preaching. It is for pastors, evangelists, or any Christian who feels called to share the Gospel with crowds outside of the church. The title is "Silver Lanterns" with a subtitle of "A guide to harbour-side singing in a restless era". The Bible verse reference for the title is Jeremiah 20:9. Size will be 9" high by 6"wide
Updates

Went on vacation/holiday

Target Market(s)

Christian pastors, missonaries, evangelists

Industry/Entity Type

religous

Requirements
Must have
• Meet Tarvelo Print Gateway guidelines for book covers

```html
<!DOCTYPE html>
<html lang="en">
<head>
<meta charset="utf-8">
<title>Silver Lanterns – Book Cover</title>
<link href="https://fonts.googleapis.com/css2?family=Bebas+Neue&family=Cinzel:wght@400&family=Sacramento&family=Montserrat:wght@700&display=swap" rel="stylesheet">
<style>
  :root {
    --sky-top: #6f6f86;
    --sky-mid: #d9d6e2;
    --paper: #f7f6f1;
    --title-blue: #3c52a3;
    --script-pink: #e8669f;
    --subtitle-navy: #263a8c;
    --author-white: #ffffff;
    --crowd-red: #e23a4a;
    --crowd-magenta: #d01f7a;
    --crowd-purple: #7a3aa8;
    --crowd-blue: #2a8fd6;
  }
  html, body {
    margin: 0;
    padding: 0;
    width: 822px;
    height: 1200px;
    overflow: hidden;
    background: #ffffff;
  }
  .cover {
    position: relative;
    width: 822px;
    height: 1200px;
    overflow: hidden;
    background: linear-gradient(180deg,
      #2c2f3c 0px,
      var(--sky-top) 70px,
      #b9b3c4 170px,
      var(--sky-mid) 300px,
      var(--paper) 520px,
      #fbfbf7 800px,
      #f4f3f6 1200px);
  }
  .author-name {
    position: absolute;
    top: 52px;
    left: 0;
    width: 100%;
    margin: 0;
    text-align: center;
    font-family: "Bebas Neue", "Oswald", sans-serif;
    font-size: 76px;
    line-height: 1;
    letter-spacing: 0.34em;
    text-indent: 0.34em;
    color: var(--author-white);
    font-weight: 400;
  }
  .title {
    position: absolute;
    top: 272px;
    left: 0;
    width: 100%;
    margin: 0;
    text-align: center;
    font-weight: 400;
  }
  .title-main {
    display: block;
    font-family: "Cinzel", "Cormorant Garamond", serif;
    font-size: 104px;
    line-height: 1;
    letter-spacing: 0.28em;
    text-indent: 0.28em;
    color: var(--title-blue);
  }
  .title-script {
    display: block;
    margin-top: -14px;
    font-family: "Sacramento", cursive;
    font-size: 138px;
    line-height: 1;
    color: var(--script-pink);
    letter-spacing: 0.01em;
  }
  .subtitle {
    position: absolute;
    top: 595px;
    left: 0;
    width: 100%;
    margin: 0;
    text-align: center;
    font-family: "Montserrat", sans-serif;
    font-weight: 700;
    font-size: 24px;
    line-height: 31px;
    color: var(--subtitle-navy);
    text-transform: uppercase;
  }
  .crowd-art {
    position: absolute;
    left: 0;
    bottom: 0;
    width: 822px;
    height: 380px;
    display: block;
  }
</style>
</head>
<body>
  <main class="cover">
    <p class="author-name">Author Name</p>

    <h1 class="title">
      <span class="title-main">SILVER</span>
      <span class="title-script">lanterns</span>
    </h1>

    <p class="subtitle">A guide to harbour-side singing<br>in a restless era</p>

    <svg class="crowd-art" viewBox="0 0 822 380" role="img" aria-label="Colourful silhouettes of a cheering crowd with raised hands, in red, magenta, purple and blue">
      <defs>
        <linearGradient id="crowdGradient" x1="0" y1="0" x2="0.35" y2="1">
          <stop offset="0" stop-color="var(--crowd-red)"/>
          <stop offset="0.4" stop-color="var(--crowd-magenta)"/>
          <stop offset="0.75" stop-color="var(--crowd-purple)"/>
          <stop offset="1" stop-color="var(--crowd-blue)"/>
        </linearGradient>
      </defs>
      <path d="M0 40 C120 10 220 60 330 80 C430 95 520 70 620 100 C700 120 770 110 822 130 L822 380 L0 380 Z" fill="url(#crowdGradient)"/>
    </svg>
  </main>
</body>
</html>
```